Stationery Design Project

I need a stationary design for our company. we are based in Houston, TX and we are called Vell Marot Lending. And we are wanting to brand our FundMendWise program, which includes our tax preparation and restoration, credit repair service. Although our business offers other programs, we are interested in mainly focusing on The FundMendWise program. We are looking for way to brand our ourselves and I believe that a great stationery design will help in achieving this goal. Our logo design is blue and light blue. the slogan is orange.

Industry/Entity Type

Business

Requirements
Must have
• Address: 30871 Birchhollow Ln. K-22
Houston, TX 77419
Tel. 832-516-3928
Fax 713-264-9187
www.vellmarotlending-example.com
info@vellmarotlending-example.com
Our Slogan: Happiness, Restored!

```html
<!DOCTYPE html>
<html lang="en">
<head>
<meta charset="utf-8">
<title>Vell Marot Lending – Business Card</title>
<link rel="stylesheet" href="https://fonts.googleapis.com/css2?family=Tinos:wght@400;700&display=swap">
<style>
  :root {
    --navy: #1c4166;
    --navy-line: #2c5585;
    --pale-blue: #c9d9ea;
    --card-white: #ffffff;
    --backdrop: #eeeeee;
    --ink-grey: #4a4f57;
  }
  * { box-sizing: border-box; margin: 0; padding: 0; }
  html, body {
    width: 1200px;
    height: 795px;
    overflow: hidden;
    background: var(--backdrop);
    font-family: "Tinos", "Times New Roman", serif;
  }
  .stationery {
    position: relative;
    width: 1200px;
    height: 795px;
  }
  .card {
    position: absolute;
    top: 254px;
    width: 500px;
    height: 286px;
  }
  /* Front */
  .card--front {
    left: 70px;
    background: var(--navy);
    color: var(--pale-blue);
    text-align: center;
  }
  .front-brand {
    position: absolute;
    top: 50px;
    left: 0;
    right: 0;
    font-size: 26px;
    letter-spacing: 1px;
  }
  .front-rule {
    position: absolute;
    left: 36px;
    right: 36px;
    border-top: 1px solid var(--pale-blue);
  }
  .front-rule--top { top: 118px; }
  .front-rule--bottom { top: 240px; }
  .services {
    position: absolute;
    top: 134px;
    left: 0;
    right: 0;
    font-size: 15px;
    line-height: 22px;
    letter-spacing: 0.5px;
    text-transform: uppercase;
  }
  .website {
    position: absolute;
    top: 204px;
    left: 0;
    right: 0;
    font-size: 14px;
    letter-spacing: 0.3px;
  }
  /* Back */
  .card--back {
    left: 630px;
    background: var(--card-white);
    color: var(--navy);
  }
  .brand-square {
    position: absolute;
    top: 24px;
    left: 300px;
    width: 110px;
    height: 100px;
    background: var(--navy);
    display: flex;
    align-items: center;
    justify-content: center;
    text-align: center;
    color: var(--pale-blue);
    font-size: 14px;
    line-height: 18px;
    padding: 8px;
  }
  .back-rule {
    position: absolute;
    left: 30px;
    border-top: 1px solid var(--navy-line);
  }
  .back-rule--top { top: 134px; width: 270px; }
  .back-rule--bottom { top: 228px; width: 440px; }
  .back-rule--bottom-2 { top: 232px; width: 440px; }
  .tagline {
    position: absolute;
    top: 142px;
    left: 30px;
    font-size: 15.5px;
    letter-spacing: 0.4px;
    text-transform: uppercase;
  }
  .contact {
    position: absolute;
    left: 30px;
    font-size: 11.5px;
    color: var(--ink-grey);
  }
  .contact--address { top: 174px; }
  .contact--lines { top: 196px; }
  .contact b { color: var(--navy); font-weight: 700; }
</style>
</head>
<body>
  <main class="stationery">
    <section class="card card--front" aria-label="Business card front">
      <p class="front-brand">Vell Marot Lending</p>
      <div class="front-rule front-rule--top"></div>
      <p class="services">
        Tax Preparation • Tax Restoration • Credit Repair<br>
        Notary Service • Ledger Preparation
      </p>
      <p class="website">www.vellmarotlending-example.com</p>
      <div class="front-rule front-rule--bottom"></div>
    </section>

    <section class="card card--back" aria-label="Business card back">
      <div class="brand-square">Vell Marot Lending</div>
      <div class="back-rule back-rule--top"></div>
      <p class="tagline">Vell Marot Lending – Happiness, Restored!</p>
      <p class="contact contact--address">
        30871 Birchhollow Ln. K-22, Houston, TX 77419 &nbsp;<b>Tel:</b> 832-516-3928
      </p>
      <p class="contact contact--lines">
        <b>Fax:</b> 713-264-9187 &nbsp;<b>E-mail:</b> info@vellmarotlending-example.com
      </p>
      <div class="back-rule back-rule--bottom"></div>
      <div class="back-rule back-rule--bottom-2"></div>
    </section>
  </main>
</body>
</html>
```